Website Voskamp detective agency

Hi all,
After my last posted job for a logo (see attached file) I now need a website for my detective agency (Recherchebureau in Dutch)
I already have the better logo then my competitors thanks to you and your colleges working with Brandforge.
Please google the word recherchebureau to see what the competition has.
I will leave it up to you.
Bare in mind I take jobs from companies (staff steeling data or products) and private people (divorce matters etc.) so it should look very professional, trustworthy and different from the others.
My company uses creativity and new/ different ways to find the truth.
I think the logo already reflects this.
Of course I need it sliced for the website builder but if you can built it too please let me know. Then I would need a template were I can upload text and photo's etc.
Target Market(s)
Corporations
Small business
Privat people
Industry/Entity Type
Detective
Coding
Coded - Design and coding required
Number of Pages Required
5+ page
Requirements
Must have
- Responsive!
- Also this logo:
- http://www.kvbwacht.nl/wp-content/uploads/2014/05/keurmerk.png
- With the line:
- Erkend door het college van toezicht en certificering
- (This means recognized by the board of oversight)
Nice to have
- Here some extra.
- It is about website trend which I think is true.
- Please use google translate because it is in Dutch.
- http://www.lumenpost.com/archive/2014/11/17/10-webdesigntrends-voor-2015/

```html
<!DOCTYPE html>
<html lang="en">
<head>
<meta charset="utf-8">
<title>Voskamp Recherchebureau</title>
<link href="https://fonts.googleapis.com/css2?family=Open+Sans:wght@400;600;700;800&display=swap" rel="stylesheet">
<style>
:root{
  --cyan:#1fa3c7;
  --cyan-dark:#178aa9;
  --ink:#2c3640;
  --ink-deep:#232b33;
  --grey-text:#6b737b;
  --light:#f3f5f7;
  --white:#ffffff;
  --rule:#dfe3e6;
}
*{margin:0;padding:0;box-sizing:border-box}
html,body{width:1200px;height:2240px;overflow:hidden;background:var(--white)}
body{font-family:"Open Sans",Arial,sans-serif;color:var(--ink);position:relative}
.section{position:absolute;left:0;width:1200px}
h2{font-weight:800;font-size:26px;text-transform:uppercase;letter-spacing:.5px}
p{font-size:13px;line-height:1.65;color:var(--grey-text)}
.btn{display:inline-block;font-size:12px;font-weight:700;text-transform:uppercase;color:var(--white);padding:9px 20px;border-radius:3px;letter-spacing:.5px}
.btn-dark{background:var(--ink)}
.btn-cyan{background:var(--cyan)}
.btn-light{background:var(--white);color:var(--ink)}

/* navigation */
.site-nav{top:0;height:64px;border-bottom:1px solid var(--rule)}
.menu{position:absolute;top:0;height:64px;display:flex;align-items:center;gap:34px;font-size:12px;font-weight:700;text-transform:uppercase}
.menu-left{left:120px}
.menu-right{left:730px}
.brand{position:absolute;left:520px;top:8px;width:160px;text-align:center}
.brand-mark{width:22px;height:22px;background:var(--ink);border-radius:50%;margin:0 auto 4px}
.brand-name{font-size:14px;font-weight:800;letter-spacing:1px;color:var(--ink)}
.search-btn{position:absolute;right:110px;top:14px;width:40px;height:36px;background:var(--cyan);border-radius:3px;display:flex;align-items:center;justify-content:center}

/* hero */
.hero{top:64px;height:320px;background:linear-gradient(90deg,#11161b 0%,#1d262e 45%,#3a4650 75%,#596772 100%)}
.hero-title{position:absolute;left:120px;top:130px;color:var(--white);font-size:34px;font-weight:800;line-height:1.25;text-transform:uppercase}
.hero-arrow{position:absolute;top:140px}
.hero-arrow.left{left:30px}
.hero-arrow.right{right:30px}

/* welcome */
.welcome{top:384px;height:206px;text-align:center;padding-top:40px}
.welcome h2{display:flex;justify-content:center;align-items:center;gap:14px;font-size:24px}
.welcome-icon{width:22px;height:22px;background:var(--ink);border-radius:50%}
.welcome p{width:860px;margin:16px auto 18px}

/* services */
.services{top:590px;height:450px;background:var(--cyan)}
.services-head{position:absolute;top:0;left:0;width:1200px;height:50px;background:var(--white)}
.services-title{position:absolute;top:28px;left:0;width:1200px;display:flex;justify-content:center;align-items:center;gap:14px;color:var(--white)}
.services-title .badge{width:46px;height:46px;border-radius:50%;background:var(--ink)}
.services-title h2{color:var(--ink);margin-top:8px}
.cards{position:absolute;top:120px;left:140px;display:flex;gap:30px}
.card{width:287px}
.card-photo{height:160px;border:4px solid var(--white)}
.card h3{color:var(--ink);font-size:13px;font-weight:800;text-transform:uppercase;margin:14px 0 6px}
.card p{color:#e9f6fa;font-size:12px}
.card .btn{margin-top:16px}

/* why / about */
.split{top:1040px;height:600px;background:var(--light)}
.about-panel{position:absolute;top:0;left:0;width:1200px;height:600px;background:var(--ink);clip-path:polygon(46% 0,100% 0,100% 100%,58% 100%)}
.why{position:absolute;left:140px;top:90px;width:420px}
.why h2,.about h2{display:flex;align-items:center;gap:14px;font-size:24px}
.why h2 .dot{width:22px;height:22px;background:var(--ink);border-radius:50%}
.why p{margin:22px 0 26px}
.about{position:absolute;left:760px;top:90px;width:310px;color:var(--white)}
.about h2{justify-content:flex-end}
.about h2 .dot{width:22px;height:22px;background:var(--white);border-radius:50%}
.about p{color:#c7ced4;margin:22px 0 26px}
.about .btn{float:right}

/* news + testimonial */
.updates{top:1640px;height:360px}
.news{position:absolute;left:140px;top:60px;width:380px}
.testimonials{position:absolute;left:590px;top:60px;width:470px}
.updates h2{font-size:20px;margin-bottom:26px}
.timeline{position:relative;padding-left:30px}
.timeline::before{content:"";position:absolute;left:8px;top:0;bottom:0;width:3px;background:var(--cyan)}
.news-item{position:relative;display:flex;gap:16px;margin-bottom:30px}
.news-item::before{content:"";position:absolute;left:-28px;top:6px;width:12px;height:12px;border-radius:50%;background:var(--white);border:3px solid var(--ink)}
.news-thumb{width:90px;height:64px;flex:none;background:linear-gradient(135deg,#4b5862,#8a99a3)}
.news-item h4{font-size:12px;font-weight:800;text-transform:uppercase;margin-bottom:4px}
.news-item p{font-size:12px}
.quote{display:flex;gap:18px;margin-bottom:28px;align-items:flex-start}
.quote-mark{font-size:60px;line-height:.8;color:var(--rule);font-weight:800}
.quote p{font-size:12px;font-style:italic}
.quote .author{font-size:12px;font-weight:700;color:var(--ink);text-align:right;margin-top:6px}
.avatar{width:52px;height:52px;border-radius:50%;flex:none;background:linear-gradient(135deg,#8c969e,#c9cfd3)}

/* footer */
.site-footer{top:2000px;height:240px;background:var(--ink)}
.footer-brand{position:absolute;left:140px;top:50px;width:240px;color:var(--white)}
.footer-brand .mark{width:46px;height:46px;border-radius:50%;border:2px solid var(--white);margin-bottom:14px}
.footer-brand .name{font-size:14px;font-weight:800;letter-spacing:1px}
.footer-brand p{color:#b8c0c6;font-size:12px;margin-top:6px}
.contact{position:absolute;left:470px;top:55px;list-style:none}
.contact li{display:flex;align-items:center;gap:12px;color:#c7ced4;font-size:12px;margin-bottom:16px}
.contact .ic{width:28px;height:28px;border-radius:50%;background:var(--cyan);display:flex;align-items:center;justify-content:center}
.newsletter{position:absolute;left:820px;top:50px;width:240px}
.newsletter h4{color:var(--white);font-size:13px;font-weight:800;text-transform:uppercase;margin-bottom:12px}
.newsletter .field{height:34px;background:var(--white);border-radius:2px;margin-bottom:10px}
.copyright{position:absolute;left:0;bottom:0;width:1200px;height:40px;background:var(--ink-deep);color:#8e979e;font-size:11px;text-align:center;line-height:40px}
</style>
</head>
<body>

<header class="section site-nav">
  <nav class="menu menu-left"><span>Home</span><span>About us</span><span>Why you choose us</span><span>News</span></nav>
  <div class="brand"><div class="brand-mark"></div><div class="brand-name">VOSKAMP</div></div>
  <nav class="menu menu-right"><span>Service</span><span>Blog</span><span>Contact us</span></nav>
  <div class="search-btn"><svg width="16" height="16" viewBox="0 0 16 16"><circle cx="6.5" cy="6.5" r="5" fill="none" stroke="#fff" stroke-width="2"/><line x1="10.5" y1="10.5" x2="15" y2="15" stroke="#fff" stroke-width="2"/></svg></div>
</header>

<section class="section hero" role="img" aria-label="Photo of a detective in a suit examining a tablet with a magnifying glass">
  <h1 class="hero-title">Voskamp<br>Recherchebureau</h1>
  <svg class="hero-arrow left" width="20" height="40" viewBox="0 0 20 40"><polyline points="16,4 4,20 16,36" fill="none" stroke="#fff" stroke-width="3"/></svg>
  <svg class="hero-arrow right" width="20" height="40" viewBox="0 0 20 40"><polyline points="4,4 16,20 4,36" fill="none" stroke="#fff" stroke-width="3"/></svg>
</section>

<section class="section welcome">
  <h2><span class="welcome-icon"></span>Welcome to Voskamp Recherchebureau</h2>
  <p>Our investigators work discreetly for companies and private clients across the Netherlands. We combine careful research, modern technology and creative thinking to uncover the facts you need. Every case is handled with strict confidentiality, clear reporting and honest advice, so you can make decisions based on evidence rather than suspicion.</p>
  <span class="btn btn-dark">Read more</span>
</section>

<section class="section services">
  <div class="services-head"></div>
  <div class="services-title"><span class="badge"></span><h2>What we do</h2></div>
  <div class="cards">
    <article class="card">
      <div class="card-photo" role="img" aria-label="Photo of hands on a laptop keyboard" style="background:linear-gradient(135deg,#2b3035,#6d757b)"></div>
      <h3>Staff steeling data</h3>
      <p>When data or stock goes missing, we trace the source quietly and deliver findings you can act on.</p>
      <span class="btn btn-light">Read more</span>
    </article>
    <article class="card">
      <div class="card-photo" role="img" aria-label="Photo of a magnifying glass over a product label" style="background:linear-gradient(135deg,#d9dde0,#9aa3a9)"></div>
      <h3>Products</h3>
      <p>We track lost or stolen goods through supply chains and document every step for legal use.</p>
      <span class="btn btn-light">Read more</span>
    </article>
    <article class="card">
      <div class="card-photo" role="img" aria-label="Photo illustrating a divorce matter" style="background:linear-gradient(135deg,#3b2f2a,#9a8276)"></div>
      <h3>Divorce matters</h3>
      <p>Personal matters need care. We gather clear facts to support you during a divorce or dispute.</p>
      <span class="btn btn-light">Read more</span>
    </article>
  </div>
</section>

<section class="section split">
  <div class="about-panel"></div>
  <div class="why">
    <h2><span class="dot"></span>Why you choose us</h2>
    <p>Licensed and recognised, our team brings years of experience from police and corporate security. We work fast, stay discreet and report in plain language. Fixed rates, no surprises and a personal contact for every case.</p>
    <span class="btn btn-cyan">Read more</span>
  </div>
  <div class="about">
    <h2><span class="dot"></span>About us</h2>
    <p>Voskamp Recherchebureau was founded to find the truth with new and different methods. From small firms to large corporations and private clients, we listen first and then investigate with precision and respect.</p>
    <span class="btn btn-light">Read more</span>
  </div>
</section>

<section class="section updates">
  <div class="news">
    <h2>Latest news</h2>
    <div class="timeline">
      <div class="news-item">
        <div class="news-thumb" role="img" aria-label="News thumbnail photo"></div>
        <div><h4>Lorem ipsum</h4><p>New certification confirms our quality standards for 2015.</p></div>
      </div>
      <div class="news-item">
        <div class="news-thumb" role="img" aria-label="News thumbnail photo"></div>
        <div><h4>Lorem ipsum</h4><p>Tips to protect company data from internal leaks.</p></div>
      </div>
    </div>
  </div>
  <div class="testimonials">
    <h2>Testimonial</h2>
    <div class="quote">
      <span class="quote-mark">“</span>
      <div><p>They found answers quickly and kept everything confidential. Highly recommended.</p><div class="author">– Ruben Haller</div></div>
      <div class="avatar" role="img" aria-label="Client portrait"></div>
    </div>
    <div class="quote">
      <span class="quote-mark">“</span>
      <div><p>Professional, calm and thorough. Their report gave us the clarity we needed.</p><div class="author">– Ruben Haller</div></div>
      <div class="avatar" role="img" aria-label="Client portrait"></div>
    </div>
  </div>
</section>

<footer class="section site-footer">
  <div class="footer-brand">
    <div class="mark"></div>
    <div class="name">VOSKAMP</div>
    <p>Lindenlaan 48, 3512 AB Utrecht</p>
  </div>
  <ul class="contact">
    <li><span class="ic"><svg width="14" height="14" viewBox="0 0 14 14"><path d="M3 1l2 3-1.5 1.5a8 8 0 0 0 5 5L10 9l3 2-1.5 2.5C6 13 1 8 .5 2.5z" fill="#fff"/></svg></span>+31 (0)30 123 4567</li>
    <li><span class="ic"><svg width="14" height="12" viewBox="0 0 14 12"><rect x="1" y="1" width="12" height="10" fill="none" stroke="#fff" stroke-width="1.5"/><polyline points="1,1 7,6 13,1" fill="none" stroke="#fff" stroke-width="1.5"/></svg></span>info@voskamp-recherche.nl</li>
    <li><span class="ic"><svg width="14" height="14" viewBox="0 0 14 14"><circle cx="7" cy="7" r="6" fill="none" stroke="#fff" stroke-width="1.5"/><line x1="1" y1="7" x2="13" y2="7" stroke="#fff" stroke-width="1.2"/><ellipse cx="7" cy="7" rx="2.5" ry="6" fill="none" stroke="#fff" stroke-width="1.2"/></svg></span>www.voskamp-recherche.nl</li>
  </ul>
  <div class="newsletter">
    <h4>News letter</h4>
    <div class="field"></div>
    <span class="btn btn-cyan">Subscribe</span>
  </div>
  <div class="copyright">Copyright © 2015 Voskamp Recherchebureau. All rights reserved.</div>
</footer>

</body>
</html>
```